Fitness Equipment & Service

I want to make the card eye catching and fun. We are called Corvane Motion Limited and we are based in Wales. We sell, install and service all types of fitness equipment from Skipping ropes, right through the Dumbbells, Kettle bells and Barbells through to state of the art Treadmills, Running Machines and Strength Equipment. We also design and install changing room furniture and lockers.

TYPOGRAPHY
We would like to use Futrura. Futura has an appearance of efficiency and forwardness. The typeface is derived
from simple geometric forms (near-perfect circles, triangles and squares) and is based on strokes of
near-even weight, which are low in contrast. This is most visible in the almost perfectly round stroke of
the o, which is nonetheless slightly ovoid.
The lowercase has tall ascenders, which rise above the cap line. The uppercase
characters present proportions similar to those of classical Roman capitals.

TYPOGRAPHIC CONSIDERATIONS
No Strike though
No Horizontal Scaling
No Drop Shadows
No Effects
Never use less than 120% Leading

OUR CORPORATE COLOURS
BRAND GUIDELINES
We were thinking that our primary colour palette consists of the Acid Green (Pantone 382) and Process Black.

We work closely with tolbrook Ltd and would like to include their name on the card somewhere. I have attached images of the other brands that we work with as an idea or the small icons I have included that illustrate what we do?. I have very kindly been given permission to use any of the images off the files that I have included below, so I hope these help. I will include these below. I would be open to suggestions if it made the card more striking Can you do it?
Updates

Hi All, Just wanted to add a few thoughts but you are the guys with the creative visions (thats why are here) We are based in Wales, UK and we would be open to lots of different ideas on a theme but must be eye catching, Bold and FUN. If you can or think that the Welsh or any dragon could be put in there then go for it (its not a must have) We have also added some ideas for colour but again its over to you!! GO FOR IT ! Thanks and look forward to your visions! Owen

Hi All, Just thought I would sen through the contact details that need to be on the card. (if you want to play around with icons instead of the wording twitter, Facebook, go for it): Corvane Motion Limited Owen Pritchard Managing Director Mob: +44 (0)7382 519 046 e-mail: sales@corvanemotion.co.uk Web: Corvanemotion.co.uk twitter: @motionPostbag Facebook: Corvane Motion Limited

Industry/Entity Type

Fitness

```html
<!DOCTYPE html>
<html lang="en">
<head>
<meta charset="utf-8">
<title>Corvane Motion Limited – Business Card</title>
<link rel="stylesheet" href="https://fonts.googleapis.com/css2?family=Libre+Baskerville:wght@700&family=Roboto:wght@400;500&display=swap">
<style>
  :root {
    --backdrop: #ece9e4;
    --card-white: #ffffff;
    --brand-blue: #2f3f9a;
    --brand-gold: #e7c765;
    --brand-navy: #2a2f6e;
    --text-light: #ffffff;
    --tile-sky: #4fc3e6;
    --tile-light: #5fb4e3;
    --tile-mid: #2f86cc;
    --tile-deep: #1a5e9c;
    --tile-night: #1b3d66;
    --tile-mist: #a9bfd0;
  }
  * { margin: 0; padding: 0; box-sizing: border-box; }
  html, body {
    width: 1200px; height: 892px; overflow: hidden;
    background: var(--backdrop);
  }
  .canvas {
    position: relative; width: 1200px; height: 892px;
    display: flex; flex-direction: column; align-items: center; justify-content: center;
    gap: 40px;
  }
  .card {
    position: relative; width: 660px; height: 378px; overflow: hidden;
    background: var(--card-white);
    box-shadow: 0 6px 18px rgba(0,0,0,0.18);
  }
  .card-shape, .back-art { position: absolute; inset: 0; }
  .brand-lockup {
    position: absolute; left: 40px; top: 150px;
    display: flex; align-items: center; gap: 16px;
  }
  .brand-dot {
    width: 74px; height: 74px; border-radius: 50%;
    background: var(--brand-blue);
  }
  .brand-name {
    font-family: 'Roboto', sans-serif; font-weight: 500;
    font-size: 20px; line-height: 1.25; color: var(--brand-navy);
    width: 150px;
  }
  .contact-block {
    position: absolute; left: 418px; top: 64px; width: 200px;
    font-family: 'Roboto', sans-serif; color: var(--text-light);
  }
  .person-name {
    font-family: 'Libre Baskerville', serif; font-weight: 700;
    font-size: 22px; line-height: 1.25; color: var(--brand-gold);
    white-space: nowrap;
  }
  .person-role { font-size: 15px; line-height: 1.3; margin-bottom: 20px; }
  .contact-line { font-size: 14px; line-height: 1.45; white-space: nowrap; }
  .contact-gap { height: 14px; }
  .icon-column {
    position: absolute; right: 12px; top: 30px;
    display: flex; flex-direction: column; gap: 9px;
  }
  .icon-chip {
    width: 18px; height: 18px; background: var(--brand-gold);
    display: flex; align-items: center; justify-content: center;
  }
</style>
</head>
<body>
<main class="canvas">

  <section class="card card-front" aria-label="Card front">
    <svg class="card-shape" width="660" height="378" viewBox="0 0 660 378" aria-hidden="true">
      <path d="M240 0 Q420 160 360 378 L660 378 L660 0 Z" fill="var(--brand-gold)"/>
      <path d="M262 0 Q438 160 378 378 L660 378 L660 0 Z" fill="var(--brand-blue)"/>
    </svg>

    <div class="brand-lockup">
      <div class="brand-dot"></div>
      <div class="brand-name">Corvane Motion Limited</div>
    </div>

    <div class="contact-block">
      <div class="person-name">Owen Pritchard</div>
      <div class="person-role">Managing Director</div>
      <div class="contact-line">+44 (0)7382 519 046</div>
      <div class="contact-line">@motionPostbag</div>
      <div class="contact-gap"></div>
      <div class="contact-line">Corvanemotion.co.uk</div>
      <div class="contact-line">Corvane Motion Limited</div>
      <div class="contact-line">sales@corvanemotion.co.uk</div>
    </div>

    <div class="icon-column" aria-hidden="true">
      <div class="icon-chip">
        <svg width="12" height="12" viewBox="0 0 12 12"><path d="M3 1 L5 3.5 L4 5 Q5 7 7 8 L8.5 7 L11 9 L9.5 11 Q4 10.5 1 3 Z" fill="var(--brand-blue)"/></svg>
      </div>
      <div class="icon-chip"></div>
      <div class="icon-chip"></div>
      <div class="icon-chip"></div>
      <div class="icon-chip">
        <svg width="12" height="12" viewBox="0 0 12 12"><rect x="1" y="2.5" width="10" height="7" fill="var(--brand-blue)"/><path d="M1 2.5 L6 6.5 L11 2.5" stroke="var(--brand-gold)" stroke-width="1" fill="none"/></svg>
      </div>
    </div>
  </section>

  <section class="card card-back" aria-label="Card back">
    <svg class="back-art" width="660" height="378" viewBox="0 0 660 378" role="img" aria-label="Checkered blue tiles of fitness equipment icons over a dumbbell photograph">
      <defs>
        <linearGradient id="back-base" x1="0" y1="0" x2="1" y2="1">
          <stop offset="0" stop-color="var(--tile-light)"/>
          <stop offset="0.5" stop-color="var(--tile-mid)"/>
          <stop offset="1" stop-color="var(--tile-deep)"/>
        </linearGradient>
      </defs>
      <rect width="660" height="378" fill="url(#back-base)"/>
      <g class="tile-grid">
        <rect x="0" y="0" width="94" height="94" fill="var(--tile-mist)"/>
        <rect x="188" y="0" width="94" height="94" fill="var(--tile-sky)"/>
        <rect x="376" y="0" width="94" height="94" fill="var(--tile-night)" opacity="0.7"/>
        <rect x="564" y="0" width="96" height="94" fill="var(--tile-sky)"/>
        <rect x="94" y="94" width="94" height="94" fill="var(--tile-sky)"/>
        <rect x="282" y="94" width="94" height="94" fill="var(--tile-night)" opacity="0.8"/>
        <rect x="470" y="94" width="94" height="94" fill="var(--tile-deep)"/>
        <rect x="0" y="188" width="94" height="94" fill="var(--tile-deep)"/>
        <rect x="188" y="188" width="94" height="94" fill="var(--tile-mist)"/>
        <rect x="376" y="188" width="94" height="94" fill="var(--tile-sky)"/>
        <rect x="564" y="188" width="96" height="94" fill="var(--tile-night)" opacity="0.7"/>
        <rect x="94" y="282" width="94" height="96" fill="var(--tile-night)" opacity="0.8"/>
        <rect x="282" y="282" width="94" height="96" fill="var(--tile-deep)"/>
        <rect x="470" y="282" width="94" height="96" fill="var(--tile-mist)"/>
      </g>
    </svg>
  </section>

</main>
</body>
</html>
```